High-end construction company needs a business card design

We need a modern looking business card that draws people in, is memorable and looks so good people will want to sick it on their fridges.
On the first side what is needed are:
Logo
My name - Tomas Verbelk
Title - Managing Director
Website - www.kravel.co.uk
Email - tomas@kravel.co.uk
Telephone - 020 5194 6381
Mobile - 07845319027
On the back side was is needed is a list of all the services we provide:
-Kitchen Renovations
-Bathroom Renovations
-House Renovations
-Garage Conversions
-Extensions
-Loft Conversions
-Conservatories
-Carpentry
-Tiling
-Electrical
-Plumbing & Heating
-Bricklaying
-Landscaping
-Decorating
-Plastering
We would like the colours to be the same shades as on the logo with grey or black for the words.
Target Market(s)
Anyone who needs building work done
Contact Information for Business Card
This business card is for a construction company which strives to deliver excellent service and quality.
The look and feel of the card should represent this.
Requirements
Must have
- On the first side what is needed are:
Logo
My name - Tomas Verbelk
Title - Managing Director
Website - www.kravel.co.uk
Email - tomas@kravel.co.uk
Telephone - 020 5194 6381
Mobile - 07845319027
Nice to have
- Cool looking features

```html
<!DOCTYPE html>
<html lang="en">
<head>
<meta charset="utf-8">
<title>Kravel Construction Ltd – Business Card</title>
<link rel="stylesheet" href="https://fonts.googleapis.com/css2?family=Arimo:wght@700&family=Nunito:wght@700&family=Open+Sans:wght@400;700&display=swap">
<style>
  :root {
    --canvas: #eef2ec;
    --card-dark: #333234;
    --brand-green: #72bb44;
    --band-light: #a9a9ad;
    --band-mid: #7c7c80;
    --ink-dark: #333234;
    --ink-white: #ffffff;
    --mark-grey: #79797c;
    --mark-faint: #48474a;
    --icon-fill: #4a4a4c;
  }
  * { margin: 0; padding: 0; box-sizing: border-box; }
  html, body {
    width: 1179px; height: 1200px; overflow: hidden;
    background: var(--canvas);
  }
  .card {
    position: absolute; left: 250px; width: 700px; height: 400px;
    border-radius: 22px; overflow: hidden; background: var(--card-dark);
  }
  .card--front { top: 190px; }
  .card--back { top: 610px; }
  .front-shape { position: absolute; inset: 0; }

  .wordmark {
    position: absolute; font-family: "Arimo", sans-serif; font-weight: 700;
    text-transform: uppercase; line-height: 1;
  }
  .wordmark--small { left: 50px; top: 102px; color: var(--mark-grey); }
  .wordmark--small .wordmark-name { font-size: 44px; letter-spacing: 1px; display: block; }
  .wordmark--small .wordmark-sub { font-size: 11.5px; letter-spacing: 2.6px; display: block; margin-top: 4px; }
  .wordmark--large { left: 0; right: 0; top: 136px; text-align: center; color: var(--mark-faint); }
  .wordmark--large .wordmark-name { font-size: 70px; line-height: 60px; height: 60px; letter-spacing: 3px; display: block; }
  .wordmark--large .wordmark-sub { font-size: 16px; line-height: 16px; height: 16px; letter-spacing: 4px; display: block; margin-top: 6px; }

  .holder-name {
    position: absolute; left: 475px; top: 63px;
    font-family: "Arimo", sans-serif; font-weight: 700; font-size: 26px; color: var(--ink-white);
  }
  .holder-title {
    position: absolute; left: 476px; top: 102px;
    font-family: "Nunito", sans-serif; font-weight: 700; font-size: 16px; color: var(--ink-dark);
  }
  .contact-list { position: absolute; left: 281px; top: 221px; list-style: none; }
  .contact-item {
    display: flex; align-items: center; height: 19px; margin-bottom: 19px;
    font-family: "Arimo", sans-serif; font-weight: 700; font-size: 19.5px; color: var(--ink-dark);
  }
  .contact-item:nth-child(3) { margin-bottom: 23px; }
  .contact-icon { width: 22px; height: 22px; margin-right: 24px; flex: none; }

  .services { position: absolute; left: 0; right: 0; top: 234px; text-align: center; }
  .services-title {
    font-family: "Open Sans", sans-serif; font-weight: 700; font-size: 15px;
    color: var(--ink-white); text-decoration: underline; margin-bottom: 2px;
  }
  .services-line {
    font-family: "Open Sans", sans-serif; font-size: 14.6px; line-height: 20.5px; color: var(--brand-green);
  }
  .services-line .dot { color: var(--ink-white); }
</style>
</head>
<body>

<section class="card card--front" aria-label="Business card front">
  <svg class="front-shape" width="700" height="400" viewBox="0 0 700 400" aria-hidden="true">
    <path d="M440,0 C300,60 168,220 185,400 L700,400 L700,0 Z" fill="var(--band-light)"/>
    <path d="M448,0 C315,55 185,215 203,400 L700,400 L700,0 Z" fill="var(--band-mid)"/>
    <path d="M455,0 C330,50 200,200 220,400 L700,400 L700,0 Z" fill="var(--brand-green)"/>
  </svg>

  <div class="wordmark wordmark--small">
    <span class="wordmark-name">Kravel</span>
    <span class="wordmark-sub">Construction Ltd</span>
  </div>

  <h1 class="holder-name">Tomas Verbelk</h1>
  <p class="holder-title">Managing Director</p>

  <ul class="contact-list">
    <li class="contact-item">
      <svg class="contact-icon" viewBox="0 0 22 22" aria-hidden="true"><circle cx="11" cy="11" r="10.5" fill="var(--icon-fill)"/><path d="M7,6 L9,6 L10,9 L8.8,10 C9.5,11.6 10.5,12.6 12,13.2 L13,12 L16,13 L16,15 C11,16 6,11 7,6 Z" fill="var(--brand-green)"/></svg>
      <span>07845319027</span>
    </li>
    <li class="contact-item">
      <svg class="contact-icon" viewBox="0 0 22 22" aria-hidden="true"><circle cx="11" cy="11" r="10.5" fill="var(--icon-fill)"/><rect x="6" y="9" width="10" height="6" rx="1.2" fill="var(--brand-green)"/><path d="M5,9 C6,5.5 16,5.5 17,9 L14.5,9 L14,7.8 L8,7.8 L7.5,9 Z" fill="var(--brand-green)"/></svg>
      <span>020 5194 6381</span>
    </li>
    <li class="contact-item">
      <svg class="contact-icon" viewBox="0 0 22 22" aria-hidden="true"><circle cx="11" cy="11" r="10.5" fill="var(--icon-fill)"/><rect x="5.5" y="7.5" width="11" height="7.5" fill="var(--brand-green)"/><path d="M5.5,7.5 L11,12 L16.5,7.5" fill="none" stroke="var(--icon-fill)" stroke-width="1"/></svg>
      <span>tomas@kravel.co.uk</span>
    </li>
    <li class="contact-item">
      <svg class="contact-icon" viewBox="0 0 22 22" aria-hidden="true"><circle cx="11" cy="11" r="10.5" fill="var(--icon-fill)"/><g fill="none" stroke="var(--brand-green)" stroke-width="1.1"><circle cx="11" cy="11" r="5.5"/><ellipse cx="11" cy="11" rx="2.4" ry="5.5"/><path d="M5.5,11 H16.5"/></g></svg>
      <span>www.kravel.co.uk</span>
    </li>
  </ul>
</section>

<section class="card card--back" aria-label="Business card back">
  <div class="wordmark wordmark--large">
    <span class="wordmark-name">Kravel</span>
    <span class="wordmark-sub">Construction Ltd</span>
  </div>

  <div class="services">
    <h2 class="services-title">Services</h2>
    <p class="services-line"><span class="dot">•</span> Kitchen Renovations <span class="dot">•</span> Bathroom Renovations <span class="dot">•</span> House Renovations</p>
    <p class="services-line"><span class="dot">•</span> Garage Conversions &nbsp;<span class="dot">•</span> Extensions <span class="dot">•</span> Loft Conversions</p>
    <p class="services-line"><span class="dot">•</span> Conservatories <span class="dot">•</span> Carpentry <span class="dot">•</span> Tiling <span class="dot">•</span> Electrical <span class="dot">•</span> Plumbing &amp; Heating</p>
    <p class="services-line"><span class="dot">•</span> Bricklaying <span class="dot">•</span> Landscaping <span class="dot">•</span> Decorating <span class="dot">•</span> Plastering</p>
  </div>
</section>

</body>
</html>
```